MarloKitchen Web Page Templates

I need two templates designed for a wholesale food/catering business, one template for the home page and the other for detail pages. The overall template should be a simple, clean and clear design. I have provided the existing logo to which the templates should directly relate.
MarloKitchen supplies food based upon traditional Ghanian recipes to a number of stores across Canberra. In addition, MarloKitchen offers catering for public and private functions across the Canberra region.
The colours in the logo represent the national colours of Ghana (yellow, green, red and black) and the website content will also include traditional Ghanian Kente patterns which will add further colour elements to the site. On this basis, the template design needs to be fairly sparse so as not to compete with the colourful content of the website detail pages.
There is no requirement for specific pages to be designed, as these will be handled in the CMS implementation.
The information provided in the Word document is only designed to provide a sense of the intended content of the website, not as a requirement for specific pages to be produced.

Target Market(s)

Retail/Wholesale food

Number of Pages Required

2 page

Font styles to use
Serif

Colors

Designer to choose colors to be used in the design.

Requirements
Must have
• Template must accommodate a responsive design
• The logo provided will form the cornerstone of the design
Nice to have
• There
Should not have
• Please do not solicit for extra work or for alternative logo design.

```html
<!DOCTYPE html>
<html lang="en">
<head>
<meta charset="utf-8">
<title>MarloKitchen – Home</title>
<link href="https://fonts.googleapis.com/css2?family=Poppins:wght@400;500;600;700;800&display=swap" rel="stylesheet">
<style>
:root{
  --gold:#f5b31a;
  --gold-deep:#e29a0c;
  --ink:#1e1e1e;
  --text:#444;
  --muted:#8a8a8a;
  --light:#f1f1f1;
  --line:#d6d6d6;
  --footer:#262626;
  --white:#fff;
}
*{box-sizing:border-box;margin:0;padding:0}
html,body{width:1200px;height:3288px;overflow:hidden}
body{font-family:"Poppins",Arial,sans-serif;color:var(--text);background:var(--white);position:relative}
.abs{position:absolute}

/* header */
.site-header{position:absolute;left:0;top:0;width:1200px;height:100px;background:var(--white)}
.brand{position:absolute;display:flex;align-items:center;gap:10px;font-weight:700;color:var(--gold-deep)}
.brand-dot{width:22px;height:22px;border-radius:50%;background:var(--gold)}
.site-header .brand{left:130px;top:18px;font-size:42px}
.contact-mail{position:absolute;left:830px;top:14px;display:flex;gap:10px;align-items:center}
.mail-icon{width:30px;height:30px;border-radius:50%;background:var(--gold);display:flex;align-items:center;justify-content:center}
.contact-mail small{display:block;font-size:11px;color:var(--muted);line-height:1.2}
.contact-mail span{font-size:14px;color:var(--ink);font-weight:500}
.main-nav{position:absolute;left:570px;top:66px;display:flex;gap:28px;font-size:14px;font-weight:600;color:var(--ink)}
.main-nav .active{color:var(--gold);border-bottom:2px solid var(--gold);padding-bottom:2px}

/* hero */
.hero{position:absolute;left:0;top:100px;width:1200px;height:340px;overflow:hidden}
.hero-photo{position:absolute;inset:0;background:linear-gradient(100deg,#c9c2b6 0%,#a88d74 30%,#6d4e3a 55%,#8d7563 75%,#c8b9aa 100%)}
.hero-copy{position:absolute;left:680px;top:70px;color:var(--white)}
.hero-copy h1{font-size:42px;font-weight:800;letter-spacing:1px;line-height:1.1}
.hero-copy p{font-size:18px;font-weight:700;color:var(--gold);margin-top:4px}
.btn{display:inline-block;background:var(--gold);color:var(--white);font-weight:700;border-radius:22px}
.hero-copy .btn{margin-top:22px;font-size:14px;padding:10px 26px}
.hero-arrow{position:absolute;top:150px;width:26px;height:40px;background:rgba(255,255,255,.85);display:flex;align-items:center;justify-content:center}
.hero-curve{position:absolute;left:0;bottom:0}

/* about */
.about-star{position:absolute;left:60px;top:720px}
.about-title{position:absolute;left:520px;top:708px;font-size:40px;font-weight:800;color:var(--ink);line-height:1.1;width:380px}
.about-text{position:absolute;left:720px;top:918px;width:440px;font-size:15px;line-height:1.55;color:var(--text)}
.about .btn{position:absolute;left:715px;top:1150px;font-size:18px;padding:10px 34px;font-weight:700}

/* section titles */
.section-title{position:absolute;left:0;width:1200px;text-align:center;font-size:34px;font-weight:700;color:var(--ink)}
.section-title::after{content:"";display:block;width:60px;height:4px;background:var(--gold);margin:10px auto 0}

/* menu */
.menu{position:absolute;left:0;top:1262px;width:1200px;height:540px;background:var(--light)}
.menu-card{position:absolute;top:166px;width:296px;height:256px;overflow:hidden;box-shadow:0 4px 10px rgba(0,0,0,.15)}
.card-photo{position:absolute;inset:0}
.card-label{position:absolute;left:0;bottom:0;width:100%;height:44px;background:rgba(255,255,255,.92);font-size:14px;font-weight:700;color:var(--ink);padding:12px 18px}
.menu-star{position:absolute;top:270px}

/* shops */
.shop-box{position:absolute;width:222px;height:100px;border:1px solid var(--line);background:var(--white);display:flex;align-items:center;justify-content:center}
.shop-mark{width:58px;height:58px;border-radius:50%;background:#d9d9d9}
.shop-mark.square{border-radius:6px}
.shop-name{position:absolute;width:222px;font-size:13px;color:var(--muted);text-align:left}

/* gallery */
.gallery{position:absolute;left:0;top:2290px;width:1200px;height:590px;background:linear-gradient(135deg,#e9e9e9 0%,#f6f6f6 40%,#dedede 70%,#f1f1f1 100%)}
.gallery-item{position:absolute;top:160px;width:372px;height:350px;overflow:hidden}
.gallery-item .caption{position:absolute;left:18px;bottom:22px;color:var(--white);font-size:16px;font-weight:700}

/* footer */
.site-footer{position:absolute;left:0;top:2880px;width:1200px;height:408px;background:var(--footer);color:var(--white)}
.site-footer .brand{left:0;width:1200px;justify-content:center;top:80px;font-size:60px}
.footer-nav{position:absolute;left:0;width:1200px;top:222px;display:flex;justify-content:center;gap:30px;font-size:14px;font-weight:600}
.follow{position:absolute;left:0;width:1200px;top:272px;display:flex;justify-content:center;align-items:center;gap:12px;font-size:13px}
.follow .rule{width:360px;height:1px;background:#555}
.social{width:22px;height:22px;border-radius:50%;background:#3a6fd8}
.copyright{position:absolute;left:0;width:1200px;top:342px;text-align:center;font-size:12px;color:#aaa}
</style>
</head>
<body>

<header class="site-header">
  <div class="brand"><span class="brand-dot"></span>MarloKitchen</div>
  <div class="contact-mail">
    <div class="mail-icon">
      <svg width="16" height="12" viewBox="0 0 16 12"><rect x="0.5" y="0.5" width="15" height="11" fill="none" stroke="#fff"/><path d="M1 1l7 6 7-6" fill="none" stroke="#fff"/></svg>
    </div>
    <div><small>E-MAIL US</small><span>hello@marlokitchen.com</span></div>
  </div>
  <nav class="main-nav">
    <span class="active">HOME</span><span>ABOUT US</span><span>MENU</span><span>SHOP</span><span>GALLERY</span><span>CONTACT US</span>
  </nav>
</header>

<section class="hero">
  <div class="hero-photo" role="img" aria-label="Chef serving a plated dish to guests at a dinner table"></div>
  <div class="hero-copy">
    <h1>FOOD CATERING</h1>
    <p>LOREM IPSUM DOLOR SIT AMET CONSEC</p>
    <span class="btn">READ MORE</span>
  </div>
  <div class="hero-arrow" style="left:0"><svg width="10" height="14"><path d="M8 1L2 7l6 6" fill="none" stroke="#333" stroke-width="2"/></svg></div>
  <div class="hero-arrow" style="right:0"><svg width="10" height="14"><path d="M2 1l6 6-6 6" fill="none" stroke="#333" stroke-width="2"/></svg></div>
  <svg class="hero-curve" width="1200" height="60" viewBox="0 0 1200 60"><path d="M0 60 L0 20 Q600 90 1200 20 L1200 60 Z" fill="#fff"/></svg>
</section>

<section class="about">
  <svg class="about-star" width="420" height="460" viewBox="0 0 420 460" role="img" aria-label="Chef garnishing a plated dish, framed in a star">
    <defs>
      <linearGradient id="starFill" x1="0" y1="0" x2="1" y2="1">
        <stop offset="0" stop-color="#e7e2da"/><stop offset="0.5" stop-color="#b9a58c"/><stop offset="1" stop-color="#8c7a62"/>
      </linearGradient>
    </defs>
    <polygon points="210,20 266,163 419,172 300,269 339,418 210,335 81,418 120,269 1,172 154,163" fill="url(#starFill)" stroke="#f5b31a" stroke-width="10" stroke-linejoin="round"/>
  </svg>
  <h2 class="about-title">MARLOKITCHEN COMMENCED IN 2004</h2>
  <p class="about-text">Coming from Ghana and with a passion for cooking I realised, through school P&amp;C fundraising, that as well as enjoying my dishes, people wanted to learn more about Ghanaian food. So I started introducing pre-packaged meals at farmers' markets and food festivals to showcase Ghanaian food far and wide. They took off! People relished the exotic flavours. So why don't you give it a go?</p>
  <span class="btn">Have a taste! Enjoy!!</span>
</section>

<section class="menu">
  <h2 class="section-title" style="top:64px">MENU</h2>
  <svg class="menu-star" style="left:62px" width="36" height="36" viewBox="0 0 40 40"><polygon points="20,2 25,15 39,15 28,24 32,38 20,30 8,38 12,24 1,15 15,15" fill="none" stroke="#c9c9c9" stroke-width="2"/></svg>
  <svg class="menu-star" style="left:1100px" width="36" height="36" viewBox="0 0 40 40"><polygon points="20,2 25,15 39,15 28,24 32,38 20,30 8,38 12,24 1,15 15,15" fill="none" stroke="#c9c9c9" stroke-width="2"/></svg>
  <div class="menu-card" style="left:132px">
    <div class="card-photo" role="img" aria-label="Bowl of sweet chilli sauce with fresh chillies" style="background:linear-gradient(160deg,#3a2a24,#b8321f 55%,#e25a2c)"></div>
    <div class="card-label">SWEET CHILLI SAUCE</div>
  </div>
  <div class="menu-card" style="left:452px">
    <div class="card-photo" role="img" aria-label="Plate of jollof rice" style="background:linear-gradient(160deg,#6b4a34,#c2572a 50%,#d9844a)"></div>
    <div class="card-label">JOLLOF RICE</div>
  </div>
  <div class="menu-card" style="left:772px">
    <div class="card-photo" role="img" aria-label="Squares of coconut sweet on a board" style="background:linear-gradient(160deg,#8d7b52,#cdbd82 50%,#e4d7a4)"></div>
    <div class="card-label">COCONUT SWEET</div>
  </div>
</section>

<section class="shops">
  <h2 class="section-title" style="top:1836px">SHOPS</h2>
  <div class="shop-box" style="left:132px;top:1944px"><span class="shop-mark square"></span></div>
  <div class="shop-name" style="left:132px;top:2058px">Saffron Lane Curry</div>
  <div class="shop-box" style="left:380px;top:1944px"><span class="shop-mark"></span></div>
  <div class="shop-name" style="left:380px;top:2058px">Ridgeway Grocer</div>
  <div class="shop-box" style="left:612px;top:1944px"><span class="shop-mark"></span></div>
  <div class="shop-name" style="left:612px;top:2058px">Hillcrest Grocer</div>
  <div class="shop-box" style="left:852px;top:1944px"><span class="shop-mark"></span></div>
  <div class="shop-name" style="left:852px;top:2058px">Kestrel Pantry, Braddon</div>
  <div class="shop-box" style="left:132px;top:2092px"><span class="shop-mark square"></span></div>
  <div class="shop-name" style="left:132px;top:2206px">Green Basket, Mawson</div>
  <div class="shop-box" style="left:380px;top:2092px"><span class="shop-mark square"></span></div>
  <div class="shop-name" style="left:380px;top:2206px">Orchard Row, Belconnen</div>
  <div class="shop-box" style="left:612px;top:2092px"><span class="shop-mark"></span></div>
  <div class="shop-name" style="left:612px;top:2206px">Northgate Grocer</div>
</section>

<section class="gallery">
  <h2 class="section-title" style="top:62px">GALLERY</h2>
  <div class="gallery-item" style="left:20px">
    <div class="card-photo" role="img" aria-label="Chicken and spinach casserole in a dish" style="background:linear-gradient(170deg,#2c2c2a,#8f8a3c 45%,#d7c06a 70%,#3a3a36)"></div>
    <div class="caption">CHICKEN AND SPINACH CASSEROLE</div>
  </div>
  <div class="gallery-item" style="left:414px">
    <div class="card-photo" role="img" aria-label="Spicy beef casserole with vegetables" style="background:linear-gradient(170deg,#3b2a22,#9a3b22 45%,#5f7a2e 70%,#2f2a26)"></div>
    <div class="caption">SPICY BEEF CASSEROLE</div>
  </div>
  <div class="gallery-item" style="left:808px">
    <div class="card-photo" role="img" aria-label="Black-eyed beans casserole in a bowl" style="background:linear-gradient(170deg,#5a4a3a,#d8c7a4 45%,#b78b52 70%,#3c3228)"></div>
    <div class="caption">BLACK-EYED BEANS CASSEROLE</div>
  </div>
</section>

<footer class="site-footer">
  <div class="brand"><span class="brand-dot"></span>MarloKitchen</div>
  <nav class="footer-nav"><span>HOME</span><span>ABOUT US</span><span>MENU</span><span>SHOP</span><span>GALLERY</span><span>CONTACT US</span></nav>
  <div class="follow"><span class="rule"></span><span>FOLLOW US</span><span class="social"></span><span class="social"></span><span class="social"></span><span class="rule"></span></div>
  <p class="copyright">Copyright © 2023 All Rights Reserved</p>
</footer>

</body>
</html>
```